Flyer-Design für Startup
Zielgruppe
Unser Unternehmen ist ein Startup in der Bildungslandschaft. Hinsichtlich dem Flyer besteht die Zielgruppe aus Studierenden im Alter zwischen 25 und 40 Jahren.
Aufgabenstellung
Die Texte sollten in der Vektor Datei bearbeitbare sein!
Die Frau im Feld sowie die Farben des Logos sollten im Flyer berücksichtigt werden. Zudem sollen die Inhalte auch grafisch aufgearbeitet werden. Format: Es soll ein 6-seitiger Zickzackfalz sein.
Unsere Webseite ist vorübergehend nur im Entwurfsmodus durch das Passwort 'torvilak4726' erreichbar.
Schriftart Helvetica!

```html
<!DOCTYPE html>
<html lang="de">
<head>
<meta charset="utf-8">
<title>Lernweit – Aufstiegsfortbildung Flyer</title>
<link rel="stylesheet" href="https://fonts.googleapis.com/css2?family=Montserrat:wght@400;500;600;700&family=Playfair+Display:wght@700;800&display=swap">
<style>
  :root {
    --page-bg: #ebebeb;
    --paper: #d9d2c4;
    --navy: #1f2b4b;
    --navy-soft: #5d6a88;
    --text: #7b7b82;
    --white: #ffffff;
    --fold: rgba(0,0,0,0.07);
  }
  * { box-sizing: border-box; margin: 0; padding: 0; }
  html, body { width: 667px; height: 1200px; overflow: hidden; }
  body {
    background: var(--page-bg);
    font-family: "Montserrat", Arial, sans-serif;
    color: var(--text);
    position: relative;
  }
  .sheet {
    position: absolute;
    left: 20px;
    width: 627px;
    height: 560px;
    display: flex;
    background: var(--paper);
    box-shadow: 0 6px 18px rgba(0,0,0,0.12);
  }
  .sheet--outer { top: 30px; }
  .sheet--inner { top: 610px; }
  .panel {
    position: relative;
    width: 209px;
    height: 560px;
    overflow: hidden;
  }
  .panel + .panel { border-left: 1px solid var(--fold); }
  .tab {
    position: absolute;
    top: 0;
    width: 100px;
    height: 72px;
    background: var(--navy);
  }
  .footer-bar {
    position: absolute;
    bottom: 0;
    height: 28px;
    background: var(--navy);
  }
  .vertical-title {
    position: absolute;
    writing-mode: vertical-rl;
    font-family: "Playfair Display", Georgia, serif;
    font-weight: 800;
    color: var(--navy-soft);
    font-size: 30px;
    letter-spacing: 0.5px;
    line-height: 1;
  }
  .vertical-title--dark { color: var(--navy); }
  .copy { position: absolute; font-size: 6.6px; line-height: 1.38; }
  .copy p { margin-bottom: 5px; text-align: justify; hyphens: auto; }
  .copy strong { color: var(--navy); font-weight: 700; }
  .heading {
    font-family: "Playfair Display", Georgia, serif;
    font-weight: 800;
    color: var(--navy);
    font-size: 9px;
    margin: 9px 0 3px;
    letter-spacing: 0.3px;
  }
  .heading:first-child { margin-top: 0; }
  .heading--large { font-size: 10px; }
  .subheading { color: var(--navy); font-weight: 600; font-size: 6.6px; margin: 4px 0 1px; }
  .list { list-style: none; padding-left: 8px; }
  .list li { position: relative; padding-left: 6px; }
  .list li::before { content: "•"; position: absolute; left: 0; }
  .list--small { font-size: 5.4px; line-height: 1.4; }
  .label { color: var(--navy); font-weight: 600; }
  .highlight { color: var(--navy); font-weight: 500; font-size: 7px; margin-top: 10px; text-align: left; }

  .cover__photo {
    position: absolute;
    inset: 0;
    background:
      radial-gradient(ellipse 45% 40% at 55% 52%, rgba(236,232,222,0.95), rgba(236,232,222,0) 70%),
      linear-gradient(180deg, #e7e4dc 0%, #cfdde2 26%, #c9d7da 42%, #cbb394 58%, #b98c55 72%, #a9773f 86%, #8e6438 100%);
  }
  .cover__tab { left: 55px; width: 100px; height: 50px; }
  .cover__brand {
    position: absolute;
    top: 58px; left: 0; right: 0;
    text-align: center;
    font-weight: 500;
    color: var(--navy);
    font-size: 17px;
  }
  .cover__title {
    position: absolute;
    top: 82px; left: 0; right: 0;
    text-align: center;
    font-family: "Playfair Display", Georgia, serif;
    font-weight: 800;
    color: var(--navy);
    font-size: 15px;
  }
  .cover__band {
    position: absolute;
    left: 0; right: 0; bottom: 0;
    height: 98px;
    background: var(--navy);
    color: var(--white);
    display: flex;
    flex-direction: column;
    justify-content: center;
    align-items: center;
    text-align: center;
    font-family: "Playfair Display", Georgia, serif;
    font-size: 12.5px;
    line-height: 1.35;
  }
  .cover__band strong { font-weight: 800; }
  .contact { margin-top: 10px; font-size: 6.6px; line-height: 1.45; font-style: normal; }
</style>
</head>
<body>

<section class="sheet sheet--outer">
  <article class="panel panel--goals">
    <div class="tab" style="left:22px;"></div>
    <h2 class="vertical-title" style="top:80px; left:160px;">Zielsetzung</h2>
    <div class="copy" style="top:150px; left:18px; width:132px;">
      <h3 class="heading">Zielsetzung</h3>
      <p>Dieser Kurs bereitet Sie auf die Prüfung zum/r geprüften Wirtschaftsfachwirt/in (RKH) vor.</p>
      <p>Die Anmeldung zur Prüfung bei der für Sie örtlich zuständigen Regionalkammer für Handel erfolgt durch den Teilnehmer und die Prüfung ist innerhalb des Maßnahmenzeitraums abzulegen.</p>
      <h3 class="heading">Vollzeit</h3>
      <p><span class="label">Kursformat :</span> Virtuelles Klassenzimmer mittels KlassRaum (ortsunabhängig)</p>
      <p><span class="label">Kursdauer:</span> 24 Wochen</p>
      <p><span class="label">Unterrichtszeiten:</span> Montag bis Freitag von 8:00 – 16:00 Uhr</p>
      <p><span class="label">Kursstart:</span> Maximale Flexibilität! Aufgrund des rollierenden Systems ist ein Kursstart zu Beginn der jeweiligen Module jederzeit modulunabhängig möglich.</p>
    </div>
    <div class="footer-bar" style="left:50px; width:130px;"></div>
  </article>

  <article class="panel panel--content">
    <div class="copy" style="top:40px; left:20px; width:170px;">
      <h3 class="heading">Kosten</h3>
      <p>Die Maßnahme ist nach AZAV durch die ZertPro als fachkundige Stelle zugelassen und erfüllt damit die Voraussetzung der Förderung über einen Bildungsgutschein durch die Arbeitsförderstelle (SGB III) bzw. das Förderbüro (SGB II), durch Rentenversicherungsträger oder nach dem Soldatenversorgungsgesetz von bis 100 % der Kosten. Die lokalen Arbeitsförderstellen bzw. Förderbüros, die Rentenversicherungsträger oder die Berufsförderungsdienste erteilen hierzu nähere Auskünfte.</p>
      <h3 class="heading">Inhalte</h3>
      <div class="subheading">Wirtschaftsbezogene Qualifikationen</div>
      <ul class="list">
        <li>Volks- und Betriebswirtschaft</li>
        <li>Rechnungswesen</li>
        <li>Recht und Steuern</li>
        <li>Unternehmensführung</li>
      </ul>
      <div class="subheading">Handlungsspezifische Qualifikationen</div>
      <ul class="list">
        <li>Betriebliches Management</li>
        <li>Investition, Finanzierung, betriebliches Rechnungswesen und Controlling</li>
        <li>Logistik</li>
        <li>Marketing und Vertrieb</li>
        <li>Führung und Zusammenarbeit</li>
      </ul>
      <h3 class="heading heading--large">Ihr persönlicher Vorteil</h3>
      <ul class="list">
        <li>Zeugnis des Trägers und/oder Teilnahmebescheinigung</li>
        <li>Bundesweit anerkannter RKH-Abschluss</li>
        <li>Querschnittsübergreifendes Fachwissen</li>
        <li>Qualifizierung zur Übernahme einer höheren Position</li>
      </ul>
      <p class="highlight">Weiterqualifizierung zum Master Professional of Business Management (RKH) ist nach Erhalt des Abschlusses möglich</p>
    </div>
  </article>

  <article class="panel panel--cover">
    <div class="cover__photo" role="img" aria-label="Foto: Frau in weißem Kleid läuft mit erhobenem Arm durch ein Weizenfeld unter hellem Himmel"></div>
    <div class="tab cover__tab"></div>
    <div class="cover__brand">Lernweit</div>
    <h1 class="cover__title">Aufstiegsfortbildung</h1>
    <div class="cover__band">
      <span>Werde jetzt <strong>Geprüfte/r</strong></span>
      <strong>Wirtschaftsfachwirt/in</strong>
      <span>(RKH)</span>
    </div>
  </article>
</section>

<section class="sheet sheet--inner">
  <article class="panel panel--intro">
    <div class="tab" style="left:28px;"></div>
    <h2 class="vertical-title vertical-title--dark" style="top:82px; left:162px;">Aufstiegsfortbildung</h2>
    <div class="copy" style="top:100px; left:16px; width:138px;">
      <p>Eine <strong>Aufstiegsfortbildung zum/zur Wirtschaftsfachwirt/-in</strong> vermittelt generalistisches Fachwissen im Bereich Handel, Industrie sowie Dienstleistungen und zählt insofern als Allrounder zu den populärsten Aufstiegsfortbildungen im kaufmännischen Bereich. Wirtschaftsfachwirte übernehmen in der Regel Führungsaufgaben und können betriebswirtschaftliche Zusammenhänge in ihrem Gesamtzusammenhang erkennen und beurteilen.</p>
      <p>Der Abschluss zum/zur Wirtschaftsfachwirt/-in ist eine echte Alternative zum klassischen Bachelorstudium an einer Hochschule. Der wesentliche Unterschied liegt in der praxisnahen Auslegung der Theorieinhalte.</p>
      <p><strong>Mit der Zuordnung auf DQR-Stufe 6 befindet sich der Abschluss auf derselben Stufe wie die Bachelor-Abschlüsse der Hochschulen.</strong></p>
    </div>
    <div class="footer-bar" style="left:40px; width:130px;"></div>
  </article>

  <article class="panel panel--requirements">
    <div class="tab" style="left:55px;"></div>
    <div class="copy" style="top:92px; left:18px; width:174px;">
      <h3 class="heading heading--large">Fachliche Voraussetzungen</h3>
      <p>Für die Teilprüfung <strong>„Wirtschaftsbezogene Qualifikationen“</strong></p>
      <ul class="list">
        <li>werden Sie zugelassen, wenn Sie eine erfolgreich bestandene Abschlussprüfung in einem anerkannten mindestens dreijährigen kaufmännischen oder verwaltenden Ausbildungsberuf haben, oder</li>
        <li>eine erfolgreich bestandene Abschlussprüfung in einem sonstigen anerkannten mindestens dreijährigen Ausbildungsberuf und danach mindestens ein Jahr Berufspraxis vorweisen können, oder</li>
        <li>eine erfolgreich bestandene Abschlussprüfung in einem anderen anerkannten Ausbildungsberuf und danach mindestens zwei Jahre Berufspraxis gesammelt haben, oder</li>
        <li>mindestens drei Jahre Berufspraxis vorweisen können.</li>
      </ul>
      <p style="margin-top:6px;">Für die Teilprüfung <strong>„Handlungsspezifische Qualifikationen“</strong> werden Sie zugelassen, wenn die abgelegte Teilprüfung „Wirtschaftsbezogene Qualifikationen“ nicht länger als fünf Jahre zurückliegt und Sie mindestens ein weiteres Jahr Berufspraxis zu den Zulassungsvoraussetzungen unter der Teilprüfung „Wirtschaftsbezogene Qualifikationen“ nachweisen können.</p>
    </div>
    <div class="footer-bar" style="left:40px; width:130px;"></div>
  </article>

  <article class="panel panel--technical">
    <h2 class="vertical-title vertical-title--dark" style="top:40px; left:12px;">Voraussetzungen</h2>
    <div class="copy" style="top:40px; left:54px; width:140px;">
      <p>Den Antrag auf Prüfung der Zulassungsvoraussetzungen erhalten Sie bei Ihrer zuständigen Regionalkammer für Handel.</p>
      <h3 class="heading">Technische Voraussetzungen</h3>
      <p>Für die Teilnahme an der Fortbildung benötigen Sie einen PC, der die folgenden Hardwareanforderungen für Fenstra-Systeme erfüllt:</p>
      <ul class="list list--small">
        <li>Computer und Prozessor: Mindestens 1,6 GHz (oder höher), 2-Core-Prozessor</li>
        <li>Arbeitsspeicher: 4,0 GB RAM</li>
        <li>Festplatte: 3,0 GB verfügbarer Speicherplatz</li>
        <li>Anzeige: Bildschirmauflösung 1024x768 Pixel</li>
        <li>Grafikkarte: Grafikhardwarebeschleunigung erfordert GrafX 9 oder höher mit TMD 2.0 oder höher für Fenstra 10</li>
        <li>Betriebssystem: Fenstra 8</li>
        <li>Video: USB 2.0 Videokamera (oder interne Kamera)</li>
      </ul>
      <h3 class="heading" style="margin-top:14px;">Kursanmeldung</h3>
      <p>Die Kursanmeldung erfolgt nach einem persönlichen Beratungsgespräch.</p>
      <p>Nehmen Sie hierzu gerne Kontakt mit uns auf. Wir freuen uns schon sehr!</p>
      <address class="contact">
        Lernweit GmbH<br>
        Ahornweg 5<br>
        32000 Musterstadt<br><br>
        www.lernweit-akademie.de<br>
        Tel.: +49-(0)5200-1234560<br>
        E-Mail: info@lernweit-akademie.de
      </address>
    </div>
  </article>
</section>

</body>
</html>
```